Concrete Construction Business Card design

We are a commercial concrete construction company based in Texas. a family owned business which our trade was passed down and taught by our grandfather whom we want represented in this design. our grandfathers nick name was "pepe" so we are wanting the letter G to be symbolized in some way with a red pepe . colors should be possibly a grey color back ground , green letter g and red pepe pepper , to be left for you to decide with integrity , concrete professionalism,and mexican heritage

Target Market(s)

general contractors, architects,inverstors, and engineers

Industry/Entity Type

Concrete

Contact Information for Business Card

Herrera Concrete Construction LLC, Ramiro Herrera, 1872 Bramblewood Ln. Millbrook Falls, TX 76590, (940)318-2746, dhslabworkllc48@quarrymail.net

```html
<!DOCTYPE html>
<html lang="en">
<head>
<meta charset="utf-8">
<title>Herrera Concrete Construction LLC – Business Card</title>
<link rel="stylesheet" href="https://fonts.googleapis.com/css2?family=Tinos:wght@400;700&display=swap">
<style>
  :root {
    --stage: #5d5d5f;
    --card: #ffffff;
    --ink: #111111;
    --accent-red: #d9281f;
    --rule: #f0a07a;
  }
  * { margin: 0; padding: 0; box-sizing: border-box; }
  html, body {
    width: 1200px;
    height: 792px;
    overflow: hidden;
    background: var(--stage);
    font-family: "Tinos", "Times New Roman", serif;
    color: var(--ink);
  }
  .card {
    position: absolute;
    left: 170px;
    top: 136px;
    width: 878px;
    height: 514px;
    background: var(--card);
  }
  .brand {
    position: absolute;
    left: 0;
    right: 0;
    top: 124px;
    text-align: center;
    font-weight: 400;
    color: var(--ink);
  }
  .brand-name {
    display: inline-flex;
    align-items: center;
    gap: 14px;
    font-size: 64px;
    line-height: 1;
  }
  .brand-dot {
    width: 22px;
    height: 22px;
    border-radius: 50%;
    background: var(--accent-red);
  }
  .brand-tagline {
    margin-top: 6px;
    font-size: 31px;
    letter-spacing: 0.3px;
    line-height: 1;
  }
  .person {
    position: absolute;
    left: 0;
    right: 0;
    top: 350px;
    text-align: center;
    font-weight: 700;
    font-size: 38px;
    line-height: 1;
  }
  .rule {
    position: absolute;
    left: 173px;
    width: 516px;
    top: 401px;
    height: 2px;
    background: var(--rule);
  }
  .contact {
    position: absolute;
    left: 0;
    right: 0;
    display: flex;
    justify-content: center;
    gap: 16px;
    font-size: 25px;
    line-height: 1;
  }
  .contact-address { top: 411px; }
  .contact-lines { top: 446px; }
  .contact-item {
    display: inline-flex;
    align-items: center;
    gap: 6px;
  }
  .icon {
    width: 22px;
    height: 22px;
    flex: none;
  }
</style>
</head>
<body>
  <main class="card">
    <div class="brand">
      <div class="brand-name">Herrera<span class="brand-dot"></span></div>
      <div class="brand-tagline">CONCRETE CONSTRUCTION LLC</div>
    </div>

    <div class="person">RAMIRO HERRERA</div>
    <div class="rule"></div>

    <div class="contact contact-address">
      <span class="contact-item">
        <svg class="icon" viewBox="0 0 22 22" aria-hidden="true">
          <rect width="22" height="22" rx="4" fill="#d9281f"/>
          <path d="M11 4a5 5 0 0 0-5 5c0 3.8 5 9 5 9s5-5.2 5-9a5 5 0 0 0-5-5z" fill="#fff"/>
          <circle cx="11" cy="9" r="2" fill="#d9281f"/>
        </svg>
        1872 Bramblewood Ln. Millbrook Falls, TX 76590
      </span>
    </div>

    <div class="contact contact-lines">
      <span class="contact-item">
        <svg class="icon" viewBox="0 0 22 22" aria-hidden="true">
          <rect width="22" height="22" rx="4" fill="#d9281f"/>
          <path d="M7.2 4.5l2.4 2.8-1.4 1.8c.9 1.9 2.3 3.3 4.2 4.2l1.8-1.4 2.8 2.4-1.5 2.2c-5.4-.4-9.6-4.6-10-10z" fill="#fff"/>
        </svg>
        (940)318-2746
      </span>
      <span class="contact-item">
        <svg class="icon" viewBox="0 0 22 22" aria-hidden="true">
          <rect width="22" height="22" rx="4" fill="#d9281f"/>
          <rect x="4.5" y="6.5" width="13" height="9.5" rx="1" fill="none" stroke="#fff" stroke-width="1.8"/>
          <path d="M4.5 7.5l6.5 4.5 6.5-4.5" fill="none" stroke="#fff" stroke-width="1.6"/>
        </svg>
        dhslabworkllc48@quarrymail.net
      </span>
    </div>
  </main>
</body>
</html>
```